KMT Compliant Dietary Supplement Label for Nutritional Company

We are in need of a label for our line of 20+ dietary supplements that are specifically formulated to balance body chemistry and match the biochemical individuality of our users based on hair tissue mineral analysis.

We have a line of approximately 20 different dietary supplements that will require use of new label in both a small (90 capsule) and large (180 capsule) size. We will start with the initial label in which Product name, Supplement Facts, and Ingredient list will need to be modified for each particular product thereafter.

The label will be placed on a transparent blue bottle with the color of lid being decided after label design. We are open to a transparent light amber bottle with black lid but blue is our preference.

We would like the majority of the label to be blue. Solid blue, fading of blue to darker blue/black, or subtle background designs are welcome with involvement of white and hints of orange. We do not want pictorial images on the label.

Label size:
Small bottle (120cc): Label size ~ 2.25” x 5.875”
Large bottle (200cc): Label size ~ 2.75” x 7.625”

Front:
-Logo near top of label with product name and description in middle and capsule count near the bottom

Right Side:
-Supplement Facts: See current product image below in brief
-Ingredient list: See current product image below in brief
-Manufactured for: See image below (This is on the left side of our current bottle and would like it moved to the bottom of the right side)

Left side:
-Suggested use: See current product image below in brief
-Leave room for possible warning statement
-Leave room for possible lot number printing
-Keep out of the reach of children.

The first files below are our current supplement label with product information. This information is what is needed on the label and will likely need some adjustments as we are updating our line of supplements and changes in KMT requirements.

The following files are the logo files and color palette.

The remaining files are some designs we came across for inspiration.

Thank you.

Target Market(s)

Health Care Profressionals

Industry/Entity Type

Health Care and Nutrition

Requirements
Nice to have
• Product name needs to be on same line in all one color
Should not have
• Pictorial Images

```html
<!DOCTYPE html>
<html lang="en">
<head>
<meta charset="utf-8">
<title>Veralin Supplement Label</title>
<link rel="stylesheet" href="https://fonts.googleapis.com/css2?family=Montserrat:ital,wght@0,400;0,500;0,600;0,700;1,300;1,400&family=Audiowide&family=Roboto+Condensed:wght@700&display=swap">
<style>
  :root {
    --backdrop: #dcdbd9;
    --navy-deep: #0b1838;
    --navy: #12275a;
    --navy-mid: #1d3f86;
    --orange: #f7862a;
    --white: #ffffff;
  }
  * { margin: 0; padding: 0; box-sizing: border-box; }
  html, body { width: 1172px; height: 1200px; overflow: hidden; background: var(--backdrop); }
  body { position: relative; font-family: "Montserrat", sans-serif; color: var(--white); }

  .label {
    position: absolute; left: 36px; top: 390px; width: 1100px; height: 420px; overflow: hidden;
    background: linear-gradient(180deg, var(--navy-deep) 0%, var(--navy) 45%, var(--navy-mid) 100%);
  }
  .label__sweep {
    position: absolute; inset: 0;
    background:
      radial-gradient(ellipse 60% 40% at 15% 10%, rgba(70,120,210,.35), transparent 70%),
      radial-gradient(ellipse 50% 40% at 90% 15%, rgba(70,120,210,.3), transparent 70%);
  }
  .label__dome { position: absolute; left: 0; top: 0; }

  .usage {
    position: absolute; left: 40px; top: 146px; width: 250px; text-align: center;
    font-size: 13.4px; line-height: 22px; font-weight: 400;
  }

  .front { position: absolute; left: 331px; top: 0; width: 440px; height: 420px; text-align: center; }
  .brand {
    position: absolute; left: 0; right: 0; top: 112px;
    font-size: 34px; font-weight: 600; line-height: 40px; color: var(--white);
  }

  .product { position: absolute; left: 0; right: 0; top: 250px; }
  .product__name { font-family: "Audiowide", sans-serif; font-weight: 400; font-size: 54px; color: var(--orange); line-height: 56px; }
  .product__desc { font-size: 23px; font-style: italic; font-weight: 300; line-height: 30px; margin-top: 2px; }
  .count { position: absolute; left: 338px; top: 366px; text-align: center; font-family: "Audiowide", sans-serif; line-height: 15px; }
  .count__num { font-size: 20px; }
  .count__unit { font-size: 13px; }

  .facts-side {
    position: absolute; left: 782px; top: 52px; width: 300px; height: 328px;
    background: linear-gradient(180deg, rgba(20,42,96,.9), rgba(29,63,134,.75));
    padding: 7px 10px;
  }
  .facts { border: 1.5px solid var(--white); border-radius: 3px; padding: 6px 8px 4px; font-size: 7.4px; line-height: 1.35; }
  .facts__title { font-family: "Roboto Condensed", sans-serif; font-size: 21px; line-height: 22px; }
  .facts__serving { font-weight: 700; border-bottom: 3px solid var(--white); padding-bottom: 3px; margin-bottom: 2px; }
  .facts table { width: 100%; border-collapse: collapse; }
  .facts th { font-weight: 500; text-align: right; vertical-align: bottom; line-height: 1.1; padding-bottom: 2px; }
  .facts td { border-top: .6px solid rgba(255,255,255,.7); padding: 1px 0; }
  .facts td.amt, .facts td.dv { text-align: right; white-space: nowrap; padding-left: 4px; }
  .facts tr.rule-thick td { border-top: 2px solid var(--white); }
  .facts tbody tr:first-child td { border-top: 1.5px solid var(--white); }
  .facts__note { border-top: 2px solid var(--white); padding-top: 2px; }
  .other, .maker { font-size: 7.4px; line-height: 1.5; margin-top: 8px; padding-left: 2px; }
  .maker { margin-top: 26px; font-weight: 700; }
  .other b { font-weight: 700; }
</style>
</head>
<body>
  <section class="label">
    <div class="label__sweep"></div>
    <svg class="label__dome" width="1100" height="420" viewBox="0 0 1100 420" aria-hidden="true">
      <ellipse cx="551" cy="-20" rx="222" ry="268" fill="#0c1a3e"/>
    </svg>

    <p class="usage">Lorem ipsum dolor sit amet, consectetuer adipiscing elit, sed diam nonummy nibh euismod tincidunt ut laoreet dolore magna aliquam erat volutpat. Ut wisi enim ad minim veniam, quis nostrud exerci tation ullamcorper suscipit</p>

    <div class="front">
      <div class="brand">Novalyte Labs</div>
      <div class="product">
        <h1 class="product__name">Veralin</h1>
        <p class="product__desc">Multiple Vitamin and<br>Miniral Suppliment</p>
      </div>
      <div class="count"><div class="count__num">90</div><div class="count__unit">Tablets</div></div>
    </div>

    <aside class="facts-side">
      <div class="facts">
        <div class="facts__title">SUPPLEMENT FACTS</div>
        <div class="facts__serving">Serving Size: 1 Capsule<br>Servings Per Container: 90</div>
        <table>
          <thead><tr><th></th><th>Amount Per<br>Serving</th><th>% Daily<br>Value</th></tr></thead>
          <tbody>
            <tr><td>Vitamin C (as ascorbic acid)</td><td class="amt">100 mg</td><td class="dv">111%</td></tr>
            <tr><td>Vitamin B5 (as D-calcium pantothenate)</td><td class="amt">100 mg</td><td class="dv">2000%</td></tr>
            <tr><td>Magnesium (as magnesium amino acid chelate)</td><td class="amt">5 mg</td><td class="dv">1%</td></tr>
            <tr><td>Zinc (as zinc amino acid chelate)</td><td class="amt">1 mg</td><td class="dv">9%</td></tr>
            <tr><td>Manganese (as manganese amino acid chelate)</td><td class="amt">1 mg</td><td class="dv">43%</td></tr>
            <tr><td>Potassium (as potassium amino acid chelate)</td><td class="amt">25 mg</td><td class="dv">1%</td></tr>
            <tr class="rule-thick"><td>Suprarenal (adrenal) powder (bovine)</td><td class="amt">100 mg</td><td class="dv">†</td></tr>
            <tr><td>Liver powder, defatted (bovine)</td><td class="amt">45 mg</td><td class="dv">†</td></tr>
            <tr><td>Betaine Hydrochloride</td><td class="amt">25 mg</td><td class="dv">†</td></tr>
          </tbody>
        </table>
        <div class="facts__note">† Daily Value not established</div>
      </div>
      <p class="other"><b>Other Ingredients:</b> Hypromellose (Vegetable Capsule),<br>Fibra-Q® (Organic Rice Fiber)</p>
      <p class="maker">Manufactured for:<br>NOVALYTE LABS, INC.<br>Mesa Vista, AZ 85000 USA</p>
    </aside>
  </section>
</body>
</html>
```